Hang Tags for New Dog Products

Hi,

I need a design put together for hangtags. The design would be for the front of a folded hangtag, which will be used for dog products.

The dog products are designed with vibrant colours, and are inspired by the outdoors and snow sports. The hang tags would also need to reflect this.

There are three different types of dog products, and if possible I would need three hangtags, same design but with the different product names.

Please find attached a sketch that I have made to give you an idea of an image I though would look ok. The hangtag will incorporate my logo, and underneath the product name.

Notes:

• My logo (attached) consists of the mountain, wolf and RV Paws. This image and writing would have to stay the same, but can the colour be made more ice or neon blue to stand out.
• The three product names are Snowdrift Harness, High Ridge Collar and Glacier Lead
• With the bottom part of the hangtag I was thinking of making it half ice or neon blue with the writings colour changing on the blue, like image “sketch” attached. The two colours don’t have to be split down the middle, like the sketch,
• With the writing for Snowdrift Harness, High Ridge Collar and Glacier Lead. I am not going with a specific writing style, I will let the designer be creative on this. The writing in the “sketch” is just an example of how I would like it to cross colours from the white to the blue.
• I have also attached my logo separately. Like I mentioned before, the logo would have to stay the same, but if the colour was made more neon or ice blue that would be great.

Target Market(s)

Dog Owners

Colors
33a6d7
0393ce
85cae6

Requirements
Must have
• Full Logo
Nice to have
• Could the Logo's colour be changed to a more ice or neon blue to stand out.

```html
<!DOCTYPE html>
<html lang="en">
<head>
<meta charset="utf-8">
<title>RV Paws Hang Tags</title>
<link rel="stylesheet" href="https://fonts.googleapis.com/css2?family=Archivo+Black&family=Roboto:wght@500&display=swap">
<style>
  :root {
    --canvas: #ffffff;
    --ink: #ffffff;
    --blue-deep: #0b2f5c;
    --blue-mid: #1474a8;
    --blue-bright: #22c3e3;
    --green-deep: #0f2a08;
    --green-mid: #2f8a12;
    --green-bright: #66d91c;
    --red-deep: #4a0208;
    --red-mid: #b5102a;
    --red-bright: #f0506c;
  }
  * { margin: 0; padding: 0; box-sizing: border-box; }
  html, body { width: 1199px; height: 1200px; overflow: hidden; background: var(--canvas); }
  .canvas { position: relative; width: 1199px; height: 1200px; }
  .hangtag {
    position: absolute; top: 350px; width: 334px; height: 499px;
    box-shadow: 0 3px 6px rgba(0,0,0,0.18);
    color: var(--ink); text-align: center;
    font-family: "Archivo Black", "Arial Black", sans-serif;
  }
  .hangtag--collar { left: 35px; background: linear-gradient(165deg, var(--blue-deep) 0%, var(--blue-mid) 45%, var(--blue-bright) 80%, var(--blue-mid) 100%); }
  .hangtag--harness { left: 432px; background: linear-gradient(165deg, var(--green-deep) 0%, var(--green-mid) 45%, var(--green-bright) 80%, var(--green-mid) 100%); }
  .hangtag--lead { left: 829px; background: linear-gradient(165deg, var(--red-deep) 0%, var(--red-mid) 45%, var(--red-bright) 80%, var(--red-mid) 100%); }
  .hang-hole {
    position: absolute; left: 50%; top: 22px; width: 94px; height: 18px;
    transform: translateX(-50%); background: var(--canvas); border-radius: 9px;
  }
  .mountain-art {
    position: absolute; left: 64px; top: 86px; width: 206px; height: 124px;
    background: linear-gradient(180deg, rgba(255,255,255,0.55), rgba(255,255,255,0.15));
    clip-path: polygon(50% 0, 100% 100%, 0 100%);
  }
  .brand-name {
    position: absolute; left: 0; right: 0; top: 222px;
    font-size: 62px; line-height: 1; letter-spacing: 1px;
  }
  .product-name {
    position: absolute; left: 0; right: 0; top: 330px;
    font-size: 38px; line-height: 40px; text-transform: uppercase;
  }
  .tagline {
    position: absolute; left: 0; right: 0; top: 420px;
    font-family: "Roboto", Arial, sans-serif; font-weight: 500;
    font-size: 11px; line-height: 14px;
  }
  .rule {
    position: absolute; left: 50%; top: 453px; width: 95px; height: 1px;
    transform: translateX(-50%); background: var(--ink);
  }
</style>
</head>
<body>
<main class="canvas">
  <article class="hangtag hangtag--collar">
    <span class="hang-hole"></span>
    <div class="mountain-art" role="img" aria-label="Snowy mountain illustration"></div>
    <div class="brand-name">RV Paws</div>
    <h2 class="product-name">High Ridge<br>Collar</h2>
    <p class="tagline">Made for Comfort, Safety, Convenience<br>&amp; Durability</p>
    <span class="rule"></span>
  </article>
  <article class="hangtag hangtag--harness">
    <span class="hang-hole"></span>
    <div class="mountain-art" role="img" aria-label="Snowy mountain illustration"></div>
    <div class="brand-name">RV Paws</div>
    <h2 class="product-name">Snowdrift<br>Harness</h2>
    <p class="tagline">Made for Comfort, Safety, Convenience<br>&amp; Durability</p>
    <span class="rule"></span>
  </article>
  <article class="hangtag hangtag--lead">
    <span class="hang-hole"></span>
    <div class="mountain-art" role="img" aria-label="Snowy mountain illustration"></div>
    <div class="brand-name">RV Paws</div>
    <h2 class="product-name">Glacier<br>Lead</h2>
    <p class="tagline">Made for Comfort, Safety, Convenience<br>&amp; Durability</p>
    <span class="rule"></span>
  </article>
</main>
</body>
</html>
```